Financing service for small businesses

Need a flyer design promoting our Financing Service, look at the attachment to see the services we offer.
We are a CPA firm and provide a wide range of services including advisory services to small businesses that are trying to obtain bank financing.
The flyer should grab the attention of prospective businesses who need assistant with their financing needs.

Target Market(s)

Small Businesses

Industry/Entity Type

It Service

Font styles to use
Serif

Colors

Designer to choose colors to be used in the design.

Requirements
Must have
• Our Logo and address
• Why use our services
• Look Professional

```html
<!DOCTYPE html>
<html lang="en">
<head>
<meta charset="utf-8">
<title>Business Financing Services – Hollis Rennard CPA</title>
<link href="https://fonts.googleapis.com/css2?family=Cormorant+Garamond:wght@500;600&family=Arimo:wght@400;700&display=swap" rel="stylesheet">
<style>
  :root {
    --brand-blue: #1f5e9c;
    --banner-blue: #0d5a9a;
    --heading-blue: #1a5b98;
    --text-gray: #4a4a4a;
    --ink: #222;
    --sky-light: #a9d1f0;
    --sky-mid: #3d7fc4;
    --glass: #1d4f86;
    --glass-deep: #0f2f55;
  }
  * { margin: 0; padding: 0; box-sizing: border-box; }
  html, body { width: 927px; height: 1200px; overflow: hidden; background: #fff; }
  .flyer { position: relative; width: 927px; height: 1200px; overflow: hidden; background: #fff; }

  .hero-photo { position: absolute; left: 0; top: 0; width: 927px; height: 1200px; }

  .brand { position: absolute; left: 28px; top: 28px; display: flex; align-items: center; gap: 20px; }
  .brand-mark { width: 80px; height: 80px; background: var(--brand-blue); }
  .brand-name {
    font-family: "Cormorant Garamond", serif; font-weight: 600; font-size: 21px;
    line-height: 23px; color: var(--brand-blue); font-variant: small-caps; letter-spacing: 0.5px;
  }

  .address {
    position: absolute; right: 45px; top: 26px; text-align: right;
    font-family: "Cormorant Garamond", serif; font-weight: 500; font-size: 16px;
    line-height: 18px; color: var(--ink); font-variant: small-caps;
  }

  .banner { position: absolute; left: 120px; top: 442px; width: 807px; height: 174px; background: rgba(13, 90, 154, 0.9); }
  .banner-title {
    position: absolute; left: 176px; top: 460px; color: #fff; white-space: nowrap;
    font-family: "Arimo", sans-serif; font-weight: 400; font-size: 51px; line-height: 68px;
  }

  .financing { position: absolute; left: 425px; top: 704px; width: 450px; }
  .financing-heading {
    font-family: "Arimo", sans-serif; font-weight: 700; font-size: 36px; color: var(--heading-blue);
    text-align: right; width: 447px; line-height: 42px; margin-bottom: 0;
  }
  .financing-intro, .financing-list {
    font-family: "Arimo", sans-serif; font-size: 17.6px; line-height: 22px; color: var(--text-gray);
  }
  .financing-list { list-style: none; margin-top: 3px; }
  .financing-list li { position: relative; padding-left: 38px; margin-bottom: 3px; }
  .financing-list li::before { content: "•"; position: absolute; left: 5px; top: 0; }

  .contact {
    position: absolute; left: 28px; top: 1070px;
    font-family: "Cormorant Garamond", serif; font-variant: small-caps; color: var(--ink);
    font-size: 22px; line-height: 23.5px; font-weight: 500;
  }
  .contact-label { color: var(--brand-blue); font-weight: 600; font-size: 21px; }

  .footer-bar { position: absolute; left: 100px; top: 1178px; width: 726px; height: 22px; background: var(--banner-blue); }
</style>
</head>
<body>
<div class="flyer">
  <svg class="hero-photo" viewBox="0 0 927 1200">
    <defs>
      <linearGradient id="skyGlass" x1="0" y1="0" x2="1" y2="1">
        <stop offset="0" stop-color="var(--sky-light)"/>
        <stop offset="0.35" stop-color="var(--sky-mid)"/>
        <stop offset="0.75" stop-color="var(--glass)"/>
        <stop offset="1" stop-color="var(--glass-deep)"/>
      </linearGradient>
    </defs>
    <path role="img" aria-label="Upward view of glass office towers against a bright sunny sky"
          d="M120,132 L830,145 C820,320 790,520 720,665 C560,700 300,690 110,650 C50,610 25,540 20,480 C30,330 70,210 120,132 Z"
          fill="url(#skyGlass)"/>
  </svg>

  <div class="brand">
    <div class="brand-mark"></div>
    <div class="brand-name">Hollis Rennard<br>Chartered<br>Accountants</div>
  </div>

  <div class="address">4410-2208 Larchmere Way SE<br>Calgary, AB, T3K 1R7</div>

  <div class="banner"></div>
  <h1 class="banner-title">Business Financing Services<br>Calgary &amp; Vancouver</h1>

  <section class="financing">
    <h2 class="financing-heading">FINANCING TYPES</h2>
    <p class="financing-intro">The types of financing used to meet financing needs might include:</p>
    <ul class="financing-list">
      <li>Conventional Term Loans (a loan that is paid back over a specific period of time, usually offered by one of the Big Banks)</li>
      <li>Operating Loans (normally used for working capital, the balance usually fluctuates with the business</li>
      <li>Revolving Lines of Credit</li>
      <li>Project Financing (secured and used to fund a very specific activity of the business)</li>
      <li>Factoring (often used against accounts receivable in order to turn receivables to cash more quickly than simply waiting for the customer to pay)</li>
      <li>Subordinated Debt</li>
      <li>Venture Capital</li>
      <li>Angel Capital</li>
    </ul>
  </section>

  <div class="contact">
    <div class="contact-label">For Contact</div>
    <div>Phone: (403) 555-0184</div>
    <div>Fax: (403) 555-0197</div>
  </div>

  <div class="footer-bar"></div>
</div>
</body>
</html>
```